PowerPoint Design

We require a sample PowerPoint design so we can pitch PPT design services to a client.

The designs do NOT need to be done in PowerPoint, but should reflect designs that *could* be created in PPT format.

We require 3 slides as part of this project:

1. A slide containing the statistical chart based on data in Figure 3.3 at http://www7.dovrimark.org/survey-releves/2006/tb-qr/ab-cd/index.cfm?LANG=ENG&VIEW=C&format=flash&PRCODE=01&TOPIC_ID=2
-> note, don't just copy and paste the existing graph - come up with something innovative and eye catching

2. Inspirational slide to motivate employees. Zorvex "inspirational quote" and select a quote you think is appropriate. Imagery should generate enthusiasm/optimism.

3. A slide of your own choosing.
Updates

Project Deadline Extended
Reason: One of the team reviewing the designs is away from office. We've decided to give other designers a chance to submit ideas. Final decision will be made on December 5th, 2011.

Target Market(s)

Business professionals

Industry/Entity Type

Zorvex

Requirements
Must have
• Must have 3 slides.

```html
<!DOCTYPE html>
<html lang="en">
<head>
<meta charset="UTF-8">
<title>Occupied private dwellings by structural type of dwelling, Canada, 2006</title>
<link href="https://fonts.googleapis.com/css2?family=Open+Sans:ital,wght@0,400;0,600;0,700;1,400&display=swap" rel="stylesheet">
<style>
  :root {
    --bg-dark: #06101d;
    --bg-mid: #2a5f9e;
    --bg-blue: #4a89d0;
    --bg-light: #c9def4;
    --card: #ffffff;
    --grid: #c8c8c8;
    --axis-text: #7a7a7a;
    --legend-text: #8a8a8a;
    --value-text: #111111;
    --badge: #e07f00;
    --badge-text: #ffffff;
    --brand: #8fbbea;
    --single: #0f4f96;
    --semi: #4a8ad0;
    --row: #e07f00;
    --duplex: #00bd7a;
    --low-rise: #23981a;
    --high-rise: #9ecb0e;
    --other: #8e8e8e;
  }
  * { margin: 0; padding: 0; box-sizing: border-box; }
  html, body { width: 1200px; height: 900px; overflow: hidden; }
  body {
    position: relative;
    font-family: "Open Sans", Arial, sans-serif;
    background: linear-gradient(135deg, var(--bg-dark) 0%, var(--bg-mid) 28%, var(--bg-blue) 58%, var(--bg-light) 100%);
  }
  .chart-card {
    position: absolute;
    left: 116px; top: 107px;
    width: 984px; height: 631px;
    background: var(--card);
    box-shadow: 0 26px 22px -14px rgba(0,0,0,0.45);
  }
  .chart {
    position: absolute; left: 0; top: 0;
    width: 1200px; height: 900px;
  }
  .axis-label { font-size: 11.5px; font-weight: 600; fill: var(--axis-text); }
  .axis-title { font-size: 14px; font-style: italic; fill: var(--legend-text); }
  .value-label { font-size: 13.5px; font-weight: 700; fill: var(--value-text); }
  .legend {
    position: absolute;
    left: 487px; top: 240px;
    width: 513px; height: 221px;
    background: var(--card);
    box-shadow: 0 2px 10px rgba(0,0,0,0.25);
    padding: 24px 0 0 34px;
    list-style: none;
  }
  .legend-item {
    display: flex; align-items: center;
    height: 25px;
    font-size: 18px; font-style: italic;
    color: var(--legend-text);
    white-space: nowrap;
  }
  .legend-swatch { width: 18px; height: 18px; margin-right: 14px; flex: none; }
  .title-badge {
    position: absolute;
    left: 819px; top: 70px;
    width: 266px; height: 266px;
    border-radius: 50%;
    background: var(--badge);
    box-shadow: 0 4px 14px rgba(0,0,0,0.35);
  }
  .title-badge h1 {
    position: absolute;
    left: 8px; top: 58px; width: 250px;
    transform: rotate(22deg);
    color: var(--badge-text);
    text-align: center;
    font-size: 24px; line-height: 30px; font-weight: 700;
    white-space: nowrap;
  }
  .title-badge .title-sub {
    display: block; font-weight: 400; font-style: italic;
  }
  .brand {
    position: absolute;
    right: 46px; top: 812px;
    display: flex; align-items: center; gap: 10px;
    color: var(--brand);
    font-size: 34px; line-height: 40px; font-weight: 700;
  }
  .brand-dot {
    width: 26px; height: 26px; border-radius: 50%;
    background: var(--brand);
  }
</style>
</head>
<body>
  <section class="chart-card"></section>

  <svg class="chart" viewBox="0 0 1200 900" role="img" aria-label="Bar chart of occupied private dwellings by structural type, Canada 2006">
    <g class="gridlines" stroke="var(--grid)" stroke-width="1">
      <line x1="263" y1="196.5" x2="817" y2="196.5"/>
      <line x1="263" y1="276.5" x2="817" y2="276.5"/>
      <line x1="263" y1="356.5" x2="817" y2="356.5"/>
      <line x1="263" y1="436.5" x2="817" y2="436.5"/>
      <line x1="263" y1="515.5" x2="817" y2="515.5"/>
      <line x1="263" y1="595.5" x2="817" y2="595.5"/>
      <line x1="263" y1="675.5" x2="817" y2="675.5" stroke="#222"/>
    </g>
    <g class="axis-labels" text-anchor="end">
      <text class="axis-label" x="248" y="200">60 %</text>
      <text class="axis-label" x="248" y="280">50 %</text>
      <text class="axis-label" x="248" y="360">40 %</text>
      <text class="axis-label" x="248" y="440">30 %</text>
      <text class="axis-label" x="248" y="519">20 %</text>
      <text class="axis-label" x="248" y="599">10 %</text>
      <text class="axis-label" x="248" y="679">0 %</text>
    </g>
    <text class="axis-title" transform="translate(186 436) rotate(-90)" text-anchor="middle">% of total occupied private dwellings</text>
    <g class="bars">
      <rect x="293" y="233" width="56" height="442" fill="var(--single)"/>
      <rect x="366" y="636" width="56" height="39" fill="var(--semi)"/>
      <rect x="439" y="630" width="56" height="45" fill="var(--row)"/>
      <rect x="512" y="633" width="56" height="42" fill="var(--duplex)"/>
      <rect x="585" y="528" width="56" height="147" fill="var(--low-rise)"/>
      <rect x="659" y="604" width="56" height="71" fill="var(--high-rise)"/>
      <rect x="732" y="662" width="56" height="13" fill="var(--other)"/>
    </g>
    <g class="values" text-anchor="middle">
      <text class="value-label" x="321" y="223">55,3 %</text>
      <text class="value-label" x="394" y="626">4,8 %</text>
      <text class="value-label" x="467" y="620">5,6 %</text>
      <text class="value-label" x="540" y="623">5,3 %</text>
      <text class="value-label" x="613" y="518">18,4 %</text>
      <text class="value-label" x="687" y="594">8,9 %</text>
      <text class="value-label" x="760" y="652">1,6 %</text>
    </g>
  </svg>

  <ul class="legend">
    <li class="legend-item"><span class="legend-swatch" style="background:var(--single)"></span>Single-detached houses</li>
    <li class="legend-item"><span class="legend-swatch" style="background:var(--semi)"></span>Semi-detached houses</li>
    <li class="legend-item"><span class="legend-swatch" style="background:var(--row)"></span>Row houses</li>
    <li class="legend-item"><span class="legend-swatch" style="background:var(--duplex)"></span>Apartments, duplex</li>
    <li class="legend-item"><span class="legend-swatch" style="background:var(--low-rise)"></span>Apartments in buildings with fewer than five storeys</li>
    <li class="legend-item"><span class="legend-swatch" style="background:var(--high-rise)"></span>Apartments in buildings with five or more storeys</li>
    <li class="legend-item"><span class="legend-swatch" style="background:var(--other)"></span>Other dwellings</li>
  </ul>

  <div class="title-badge">
    <h1>Occupied<br>private dwellings<br>by structural type<br>of dwelling,<span class="title-sub">Canada, 2006</span></h1>
  </div>

  <div class="brand"><span class="brand-dot"></span>Nortide</div>
</body>
</html>
```